Luma Harbor Vow Studio, Inc.

Luma Harbor Vow Studio Business Card design for Cardlyne. Clean, contemporary, creative, colorful (using colors provided). ONE SIDE SHOULD INCLUDE logo, www.lumaharborvowstudio.com, @sayidoatluma. OTHER SIDE SHOULD INCLUDE Delia Brennan. Owner & Officiant. Port Avena, Solmara. 555.014.2871. delia@lumaharborvowstudio.com. Colors are blue #58AA9E
and golden #e2bf80)

Target Market(s)

Destination Wedding Clients in the United States

Contact Information for Business Card

Delia Brennan
Owner & Officiant
Port Avena, Solmara
555.014.2871
delia@lumaharborvowstudio.com

Font styles to use
Sans Serif

Requirements
Must have
• Colorful (colors are blue #58AA9E
• and golden #e2bf80), clean, contemporary. ONE SIDE SHOULD INCLUDE logo, www.lumaharborvowstudio.com, @sayidoatluma. Other side should include Delia Brennan. Owner & Officiant. Port Avena, Solmara. 555.014.2871. delia@lumaharborvowstudio.com
Nice to have
• I would like to see a version that includes my bio photo, and one that doesn't include the bio photo

```html
<!DOCTYPE html>
<html lang="en">
<head>
<meta charset="utf-8">
<title>Luma Harbor Vow Studio – Business Card</title>
<link rel="stylesheet" href="https://fonts.googleapis.com/css2?family=Josefin+Sans:wght@300;400&family=Roboto+Condensed:wght@300;400&display=swap">
<style>
  :root {
    --page: #d6d6d8;
    --card: #ffffff;
    --ink: #5b5b5e;
    --ink-soft: #6e6e72;
    --rule: #58aa9e;
    --photo-top: #d9ab6f;
    --photo-mid: #c99f6c;
    --photo-low: #9e9a98;
    --grad-top: #c7c29f;
    --grad-mid: #9eab9d;
    --grad-low: #5b8faf;
    --logo: #ffffff;
  }
  * { box-sizing: border-box; margin: 0; padding: 0; }
  html, body { width: 1200px; height: 1200px; overflow: hidden; }
  body {
    background: var(--page);
    display: flex;
    align-items: center;
    justify-content: center;
    gap: 60px;
  }
  .card {
    width: 400px;
    height: 700px;
    background: var(--card);
    display: flex;
    flex-direction: column;
    box-shadow: 0 12px 30px rgba(0,0,0,0.18);
  }
  .card__photo {
    height: 540px;
    background: linear-gradient(180deg, var(--photo-top) 0%, var(--photo-mid) 70%, var(--photo-low) 100%);
  }
  .card__details {
    flex: 1;
    display: flex;
    flex-direction: column;
    align-items: center;
    justify-content: center;
    padding: 0 32px;
    color: var(--ink);
    font-family: "Roboto Condensed", sans-serif;
  }
  .name {
    font-family: "Josefin Sans", sans-serif;
    font-weight: 400;
    font-size: 34px;
    font-variant: small-caps;
    letter-spacing: 0.5px;
    line-height: 1;
  }
  .role {
    font-size: 16px;
    letter-spacing: 1.5px;
    color: var(--ink-soft);
    margin-top: 6px;
  }
  .dotted {
    width: 100%;
    border-top: 1.5px dotted var(--rule);
    margin: 8px 0;
  }
  .contact-row {
    display: flex;
    width: 100%;
    justify-content: center;
    font-size: 18px;
  }
  .contact-row span { padding: 0 14px; }
  .contact-row span + span { border-left: 1.5px dotted var(--rule); }
  .email { font-size: 19px; letter-spacing: 0.6px; }

  .card__brand {
    height: 540px;
    background: linear-gradient(180deg, var(--grad-top) 0%, var(--grad-mid) 45%, var(--grad-low) 100%);
    display: flex;
    flex-direction: column;
    align-items: center;
    justify-content: center;
    gap: 16px;
    padding-bottom: 60px;
  }
  .brand-dot {
    width: 44px;
    height: 44px;
    border-radius: 50%;
    border: 2px solid var(--logo);
  }
  .brand-name {
    font-family: "Josefin Sans", sans-serif;
    font-weight: 300;
    font-size: 30px;
    color: var(--logo);
    letter-spacing: 1px;
    text-align: center;
    line-height: 1.25;
  }
  .card__links {
    flex: 1;
    display: flex;
    flex-direction: column;
    align-items: center;
    justify-content: center;
    padding: 0 32px;
    font-family: "Roboto Condensed", sans-serif;
    color: var(--ink);
    font-size: 19px;
    letter-spacing: 0.8px;
  }
</style>
</head>
<body>
  <section class="card card--front">
    <div class="card__photo" role="img" aria-label="Portrait photo of the owner and officiant"></div>
    <div class="card__details">
      <h1 class="name">Delia Brennan</h1>
      <p class="role">Owner &amp; Officiant</p>
      <div class="dotted"></div>
      <p class="contact-row"><span>555.014.2871</span><span>Port Avena, Solmara</span></p>
      <div class="dotted"></div>
      <p class="email">delia@lumaharborvowstudio.com</p>
    </div>
  </section>

  <section class="card card--back">
    <div class="card__brand">
      <div class="brand-dot"></div>
      <p class="brand-name">Luma Harbor<br>Vow Studio</p>
    </div>
    <div class="card__links">
      <p>@sayidoatluma</p>
      <div class="dotted"></div>
      <p>www.lumaharborvowstudio.com</p>
    </div>
  </section>
</body>
</html>
```